QRV Stationery Design Project

Dear Designers,
We need a new stationery design for company to match our new logo.
Designers should provide a design for the following:
1. Business Card: 3.5x2 Inches.
2. Letterhead: A4 size.
3. Envelops: 25x35.5 Cm.
You can keep the Arabic name at the bottom of the logo Or you can use the separate attached Arabic Name.
Please refer to the attached logo guide for design information.
Sample Business Card information:
Name: Tariq Nawaf
Position: Operation Manager
Tel: +966 920007714 Ex. 500
Fax: +966 (3)8842617
Mob: +966 (5)00387251
email: tariq@qrv-example.com.sa
URL: www.qrv-example.com.sa
Address:
Al Wadi Tower, Suite 303
Nasser bin Salem Str.
Khobar, 31847
Saudi Arabia
Updates
Dear All,
Please note, we had uploaded our logo along with Arabic writing in Adobe illustrator format (.ai).
Regards,
Khalid
Dear All,
A sample data for the business card had been added as per your request.
Regards,
Khalid

```html
<!DOCTYPE html>
<html lang="en">
<head>
<meta charset="utf-8">
<title>QRV Business Card</title>
<link rel="stylesheet" href="https://fonts.googleapis.com/css2?family=Open+Sans:wght@400;600;700&family=Cairo:wght@700&display=swap">
<style>
  :root {
    --navy: #0f2f57;
    --grey: #9a9c9f;
    --ink: #3a3a3c;
    --paper: #ffffff;
    --backdrop: #2f2f31;
  }
  * { margin: 0; padding: 0; box-sizing: border-box; }
  html, body { width: 1200px; height: 472px; overflow: hidden; }
  body {
    background: var(--backdrop);
    font-family: "Open Sans", Arial, sans-serif;
    position: relative;
  }
  .card {
    position: absolute;
    width: 526px;
    height: 302px;
    background: var(--paper);
    border-radius: 14px;
    overflow: hidden;
  }
  .card--front { left: 62px; top: 74px; }
  .card--back { left: 622px; top: 77px; }

  .brand {
    position: absolute;
    display: flex;
    align-items: center;
    gap: 14px;
    color: var(--navy);
    font-weight: 700;
    font-size: 56px;
    line-height: 1;
    letter-spacing: 1px;
  }
  .brand__dot {
    width: 22px; height: 22px;
    border-radius: 50%;
    background: var(--navy);
  }
  .card--front .brand { left: 168px; top: 40px; }
  .card--back .brand { left: 188px; top: 100px; }

  .brand-arabic {
    position: absolute;
    left: 0; right: 0;
    top: 116px;
    text-align: center;
    font-family: "Cairo", "Open Sans", sans-serif;
    font-weight: 700;
    font-size: 22px;
    color: var(--navy);
    direction: rtl;
    padding-right: 30px;
  }

  .contacts {
    position: absolute;
    left: 86px;
    top: 154px;
    font-size: 13.5px;
    color: var(--ink);
    line-height: 18px;
    z-index: 2;
  }
  .contacts__row { display: flex; gap: 18px; }
  .contacts__item { display: flex; align-items: center; gap: 5px; width: 130px; }
  .contacts__item:nth-child(2) { width: auto; }
  .contacts__item svg { width: 11px; height: 11px; fill: var(--ink); flex: none; }
  .address { margin-top: 2px; }

  .waves { position: absolute; left: 0; top: 0; width: 526px; height: 302px; }

  .holder-name {
    position: absolute;
    right: 56px;
    bottom: 24px;
    color: var(--paper);
    font-weight: 700;
    font-size: 17px;
  }

  .website {
    position: absolute;
    left: 0; right: 0;
    top: 206px;
    text-align: center;
    font-size: 13px;
    letter-spacing: 2px;
    color: var(--navy);
    font-weight: 600;
  }
</style>
</head>
<body>

<section class="card card--front">
  <svg class="waves" viewBox="0 0 526 302" aria-hidden="true">
    <path d="M0 216 C80 236 180 250 260 240 C340 230 400 190 526 184 L526 196 C410 200 350 242 260 254 C180 264 80 250 0 228 Z" fill="var(--grey)"/>
    <path d="M0 236 C80 256 180 272 270 262 C350 254 420 214 526 206 L526 302 L0 302 Z" fill="var(--navy)"/>
    <path d="M0 244 C90 266 190 280 280 270 C360 262 430 226 526 216" fill="none" stroke="var(--grey)" stroke-width="2"/>
  </svg>

  <div class="brand"><span class="brand__name">QRV</span><span class="brand__dot"></span></div>
  <div class="brand-arabic" lang="ar">كيو آر في</div>

  <div class="contacts">
    <div class="contacts__row">
      <span class="contacts__item">
        <svg viewBox="0 0 12 12"><path d="M2.5 1 4.5 1 5.3 3.5 4 4.5C4.6 6 6 7.4 7.5 8L8.5 6.7 11 7.5 11 9.5C11 10.3 10.3 11 9.5 11 5 11 1 7 1 2.5 1 1.7 1.7 1 2.5 1Z"/></svg>
        123-456-7890
      </span>
      <span class="contacts__item">
        <svg viewBox="0 0 12 12"><path d="M1 3h10v7H1z M1 3l5 4 5-4" stroke="#fff" stroke-width="0.8"/></svg>
        info@qrv-example.com.sa
      </span>
    </div>
    <div class="contacts__row">
      <span class="contacts__item">
        <svg viewBox="0 0 12 12"><path d="M2 6 3 3h6l1 3v3H9v1H7.5V9h-3v1H3V9H2z"/></svg>
        123-456-7890
      </span>
      <span class="contacts__item">
        <svg viewBox="0 0 12 12"><circle cx="6" cy="6" r="5"/></svg>
        www.website.com
      </span>
    </div>
    <div class="address">Street Name, City Name<br>State, City Zip 123 4560</div>
  </div>

  <div class="holder-name">YOUR NAME</div>
</section>

<section class="card card--back">
  <div class="brand"><span class="brand__name">QRV</span><span class="brand__dot"></span></div>
  <div class="website">www.website.com</div>
</section>

</body>
</html>
```